Professional BBQ Cleaning Flyer (Before & After Focus)

We need a clean, professional double-sided A5 flyer for a BBQ cleaning business.
This flyer will be handed directly to:
Property managers
Retirement villages
Over 50s communities
Resorts / body corporate
The design must feel professional, trustworthy, and easy to read β not cluttered or cheap.
π― Goal
Use a strong before & after BBQ image to show the value of the service, and position the business as reliable for communal BBQ cleaning.
π Size & Format
A5 (148 x 210mm)
Portrait (vertical)
Double-sided
Print-ready (with bleed)
π¨ Style & Branding
Colours: Red, Black, White
Clean, modern, minimal
Strong, easy-to-read fonts (important for older audience)
Plenty of white space
No emojis, no clutter, no cheap design elements
π₯ FRONT SIDE (IMPORTANT β MAIN FOCUS)
Must include:
Headline:
Professional BBQ Cleaning
For Shared & Communal Areas
Subheadline:
Keep your BBQs clean, safe, and ready for residents & guests
Main Visual :
Side-by-side BEFORE & AFTER BBQ
This is the main focus of the flyer
Must be realistic and high quality
Labels under images:
BEFORE β Greasy β’ Dirty β’ Unsafe
AFTER β Clean β’ Hygienic β’ Ready to Use
Short Bullet Points:
Deep clean of grills, burners & internal components
Ideal for retirement villages, resorts & body corporate
Multiple BBQs cleaned in one visit
Trust Line:
Fully insured & police checked
Call to Action (bottom):
Get a Quote or Book a Service
0438 254 091
www.grillshinecrew.com.au
β¬ BACK SIDE (CREDIBILITY & DETAIL)
Headline:
Trusted by Property Managers & Facilities Teams
Whatβs Included:
Full dismantle and deep clean
Removal of grease, carbon & built-up residue
Grills, burners, trays & surfaces cleaned
Reassembled and checked
Why Choose Us:
Professional, reliable service
Works around your schedule
Ideal for high-use communal BBQ areas
One-off or ongoing maintenance
Ideal For:
Retirement villages
Apartment complexes
Resorts
Body corporate properties
Closing Line:
Keep your shared BBQ areas clean, safe, and presentable year-round
Contact:
Grill Shine Crew
0438 254 091
www.grillshinecrew.com.au
grillshinecrew@mailbox-demo.com.au

```html
<!DOCTYPE html>
<html lang="en">
<head>
<meta charset="utf-8">
<title>Grill Shine Crew – Communal BBQ Cleaning Flyer</title>
<link href="https://fonts.googleapis.com/css2?family=Bebas+Neue&family=Poppins:ital,wght@0,400;0,500;0,600;0,700;0,800;1,700;1,800&display=swap" rel="stylesheet">
<style>
  :root{
    --red:#f23434;
    --black:#0b0b0b;
    --white:#ffffff;
    --grey:#8a8a8a;
    --backdrop:#cccccc;
  }
  *{box-sizing:border-box;margin:0;padding:0}
  html,body{width:1200px;height:926px;overflow:hidden;background:var(--backdrop)}
  body{position:relative;font-family:'Poppins',sans-serif;color:var(--black)}
  .flyer{position:absolute;top:86px;width:488px;height:754px;background:var(--white);overflow:hidden}
  .flyer--front{left:89px}
  .flyer--back{left:623px}

  .brand{position:absolute;top:40px;left:0;width:100%;display:flex;align-items:center;justify-content:center;gap:12px}
  .brand__dot{width:44px;height:44px;border-radius:50%;background:var(--red)}
  .brand__name{font-family:'Poppins',sans-serif;font-weight:800;font-size:27px;color:var(--black);letter-spacing:-0.3px}

  .headline{position:absolute;left:0;width:100%;text-align:center;font-family:'Bebas Neue',sans-serif;line-height:1;letter-spacing:-0.5px}
  .headline--pro{top:124px;font-size:96px;color:var(--black)}
  .headline--bbq{top:201px;font-size:96px;color:var(--red)}
  .tagbar{position:absolute;top:293px;left:33px;width:423px;height:38px;background:var(--black);color:var(--white);font-weight:800;font-size:21px;display:flex;align-items:center;justify-content:center;letter-spacing:-0.2px}
  .subline{position:absolute;top:340px;left:0;width:100%;text-align:center;font-weight:800;font-style:italic;font-size:16.5px;line-height:20px;color:var(--grey)}

  .showcase{position:absolute;top:395px;left:0;width:100%;height:277px;background:var(--black)}
  .story{position:absolute;left:0;top:0;width:203px;height:100%;background:var(--red);color:var(--white);padding:13px 12px 0 36px;font-size:8.6px;line-height:12px;font-weight:500;text-align:justify}
  .story p+p{margin-top:12px}

  .shot{position:absolute;border:2px solid #e8e8e8}
  .flyer--back .shot{border:2px solid var(--black)}
  .shot__photo{width:100%;height:100%}
  .photo--grill-dirty{background:linear-gradient(160deg,#8a8683 0%,#4b4440 45%,#2a2522 100%)}
  .photo--grill-clean{background:linear-gradient(160deg,#c9cbcd 0%,#7e8286 45%,#2f3134 100%)}
  .photo--kettle-dirty{background:linear-gradient(170deg,#a08564 0%,#4a3a2c 50%,#5b7a3a 100%)}
  .photo--kettle-clean{background:linear-gradient(170deg,#9a9c9e 0%,#2d2f31 50%,#6f8f46 100%)}
  .photo--oven-dirty{background:linear-gradient(170deg,#8e8e8e 0%,#3a2f28 55%,#6a4a2e 100%)}
  .photo--oven-clean{background:linear-gradient(170deg,#d4d4d4 0%,#3a3b3d 55%,#1c1c1c 100%)}
  .shot__tag{position:absolute;top:0;left:0;height:14px;padding:0 7px;background:var(--red);color:var(--white);font-weight:700;font-size:7.5px;line-height:14px;letter-spacing:0.2px}
  .caption{position:absolute;width:120px;text-align:center;font-size:6.6px;font-weight:600}
  .caption--before{color:var(--red)}
  .caption--after{color:var(--white)}
  .flyer--back .caption--after{color:var(--black)}

  .cta{position:absolute;top:692px;left:41px;font-weight:800;font-size:17px;line-height:18px;color:var(--black)}
  .cta__accent{color:var(--red)}
  .contact{position:absolute;top:692px;right:41px;text-align:right}
  .contact__phone{font-weight:800;font-size:17px;line-height:18px;color:var(--red)}
  .contact__web{font-weight:800;font-style:italic;font-size:15px;line-height:20px;color:var(--grey)}

  .headline--trust{top:126px;font-size:63px;color:var(--black)}
  .headline--teams{top:183px;font-size:43px;color:var(--red)}

  .details{position:absolute;top:253px;left:34px;width:420px;height:101px;display:flex;text-align:center;color:var(--white)}
  .details__col{padding-top:10px}
  .details__col--included{width:169px;background:var(--black)}
  .details__col--why{width:149px;background:var(--red)}
  .details__col--ideal{width:102px;background:var(--black)}
  .details__title{font-weight:800;font-size:11.5px;line-height:12px;margin-bottom:4px}
  .details__title span{color:var(--red);display:block}
  .details__col--why .details__title span{color:var(--white)}
  .details__list{list-style:none;font-size:6.6px;font-weight:600;line-height:11.8px}

  .closing{position:absolute;top:620px;left:0;width:100%;height:52px;background:var(--red);color:var(--white);text-align:center;font-weight:800;font-style:italic;font-size:16.5px;line-height:20px;padding-top:6px}
</style>
</head>
<body>

<section class="flyer flyer--front">
  <div class="brand"><span class="brand__dot"></span><span class="brand__name">Grill Shine Crew</span></div>
  <h1 class="headline headline--pro">PROFESSIONAL</h1>
  <div class="headline headline--bbq">BBQ CLEANING</div>
  <div class="tagbar">FOR SHARED &amp; COMMUNAL AREAS</div>
  <p class="subline">Keep your BBQs Clean Safe, and<br>Ready for Residents &amp; Guests</p>

  <div class="showcase">
    <div class="story">
      <p>At Grill Shine Crew, we understand that for most Australians, a BBQ is more than just a tool—it's the heart of Aussie gatherings. That's why we offer a professional BBQ cleaning service that goes beyond the surface. Our expert cleaners dismantle and meticulously clean every part of your BBQ, restoring it to peak condition. Serving the Sunshine Coast, we bring high standards of care right to your door, ensuring your BBQ is always ready for the next cookout.</p>
      <p>We believe in delivering a cleaner BBQ that enhances the safety and taste of your food, so you can focus so you can focus on what matters most—enjoying time with family and friends.</p>
    </div>

    <div class="shot" style="left:225px;top:16px;width:104px;height:104px">
      <div class="shot__photo photo--grill-dirty" role="img" aria-label="Built-in stainless BBQ covered in grease before cleaning"></div>
      <span class="shot__tag">BEFORE</span>
    </div>
    <div class="caption caption--before" style="left:217px;top:124px">Greasy • Dirty • Unsafe</div>
    <div class="shot" style="left:344px;top:16px;width:104px;height:104px">
      <div class="shot__photo photo--grill-dirty" role="img" aria-label="Second built-in BBQ with carbon build-up before cleaning"></div>
      <span class="shot__tag">BEFORE</span>
    </div>
    <div class="caption caption--before" style="left:336px;top:124px">Greasy • Dirty • Unsafe</div>

    <div class="shot" style="left:225px;top:144px;width:104px;height:104px">
      <div class="shot__photo photo--grill-clean" role="img" aria-label="Built-in stainless BBQ after cleaning"></div>
      <span class="shot__tag">AFTER</span>
    </div>
    <div class="caption caption--after" style="left:217px;top:253px">Clean • Hygienic • Ready to Use</div>
    <div class="shot" style="left:344px;top:144px;width:104px;height:104px">
      <div class="shot__photo photo--grill-clean" role="img" aria-label="Second built-in BBQ after cleaning"></div>
      <span class="shot__tag">AFTER</span>
    </div>
    <div class="caption caption--after" style="left:336px;top:253px">Clean • Hygienic • Ready to Use</div>
  </div>

  <div class="cta"><span class="cta__accent">GET A QUOTE</span> OR<br>BOOK A SERVICE</div>
  <div class="contact">
    <div class="contact__phone">0438-254-091</div>
    <div class="contact__web">www.grillshinecrew.com.au</div>
  </div>
</section>

<section class="flyer flyer--back">
  <div class="brand"><span class="brand__dot"></span><span class="brand__name">Grill Shine Crew</span></div>
  <h1 class="headline headline--trust">TRUSTED BY PROPERTY</h1>
  <div class="headline headline--teams">MANAGERS &amp; FACILITIES TEAMS</div>

  <div class="details">
    <div class="details__col details__col--included">
      <h2 class="details__title"><span>WHAT'S</span>INCLUDED:</h2>
      <ul class="details__list">
        <li>Full dismantle and deep clean</li>
        <li>Removal of grease, carbon &amp; built-up residue</li>
        <li>Grills, burners, trays &amp; surfaces cleaned</li>
        <li>Reassembled and checked</li>
      </ul>
    </div>
    <div class="details__col details__col--why">
      <h2 class="details__title"><span>WHY</span>CHOOSE US:</h2>
      <ul class="details__list">
        <li>Professional, reliable service</li>
        <li>Works around your schedule</li>
        <li>Ideal for high-use communal BBQ areas</li>
        <li>One-off or ongoing maintenance</li>
        <li>Fully insured &amp; police checked</li>
      </ul>
    </div>
    <div class="details__col details__col--ideal">
      <h2 class="details__title"><span>IDEAL</span>FOR:</h2>
      <ul class="details__list">
        <li>Retirement villages</li>
        <li>Apartment complexes</li>
        <li>Resorts</li>
        <li>Body corporate properties</li>
      </ul>
    </div>
  </div>

  <div class="shot" style="left:34px;top:370px;width:97px;height:97px"><div class="shot__photo photo--grill-dirty" role="img" aria-label="Hooded BBQ with greasy hotplate before cleaning"></div><span class="shot__tag">BEFORE</span></div>
  <div class="caption caption--before" style="left:23px;top:471px">Greasy • Dirty • Unsafe</div>
  <div class="shot" style="left:141px;top:370px;width:97px;height:97px"><div class="shot__photo photo--grill-clean" role="img" aria-label="Hooded BBQ after cleaning"></div><span class="shot__tag">AFTER</span></div>
  <div class="caption caption--after" style="left:130px;top:471px">Clean • Hygienic • Ready to Use</div>
  <div class="shot" style="left:249px;top:370px;width:97px;height:97px"><div class="shot__photo photo--kettle-dirty" role="img" aria-label="Portable kettle BBQ with burnt lid before cleaning"></div><span class="shot__tag">BEFORE</span></div>
  <div class="caption caption--before" style="left:238px;top:471px">Greasy • Dirty • Unsafe</div>
  <div class="shot" style="left:356px;top:370px;width:97px;height:97px"><div class="shot__photo photo--kettle-clean" role="img" aria-label="Portable kettle BBQ after cleaning"></div><span class="shot__tag">AFTER</span></div>
  <div class="caption caption--after" style="left:345px;top:471px">Clean • Hygienic • Ready to Use</div>

  <div class="shot" style="left:34px;top:495px;width:97px;height:97px"><div class="shot__photo photo--oven-dirty" role="img" aria-label="Oven interior with baked-on grime before cleaning"></div><span class="shot__tag">BEFORE</span></div>
  <div class="caption caption--before" style="left:23px;top:596px">Greasy • Dirty • Unsafe</div>
  <div class="shot" style="left:141px;top:495px;width:97px;height:97px"><div class="shot__photo photo--oven-clean" role="img" aria-label="Oven interior after cleaning"></div><span class="shot__tag">AFTER</span></div>
  <div class="caption caption--after" style="left:130px;top:596px">Clean • Hygienic • Ready to Use</div>
  <div class="shot" style="left:249px;top:495px;width:97px;height:97px"><div class="shot__photo photo--oven-dirty" role="img" aria-label="Second oven with stained racks before cleaning"></div><span class="shot__tag">BEFORE</span></div>
  <div class="caption caption--before" style="left:238px;top:596px">Greasy • Dirty • Unsafe</div>
  <div class="shot" style="left:356px;top:495px;width:97px;height:97px"><div class="shot__photo photo--oven-clean" role="img" aria-label="Second oven after cleaning"></div><span class="shot__tag">AFTER</span></div>
  <div class="caption caption--after" style="left:345px;top:596px">Clean • Hygienic • Ready to Use</div>

  <p class="closing">Keep your shared BBQ areas clean<br>safe, and presentable year-round</p>

  <div class="cta"><span class="cta__accent">GET A QUOTE</span> OR<br>BOOK A SERVICE</div>
  <div class="contact">
    <div class="contact__phone">0438-254-091</div>
    <div class="contact__web">www.grillshinecrew.com.au</div>
  </div>
</section>

</body>
</html>
```